Re-Design Qarnelo.com make it more professional looking

We want to re-design this website, we are currently not happy with existing design. Some of the design examples are listed below.

https://lumbek.com/
https://www.fastroe.com/
https://www.kelvaro.com/projects/
https://www.brightmoss.com/

The content on the website is final, there will be no change in the content. We just need to re-design the site. Features page on the site is very important and need to be layout very well.

Industry/Entity Type

It Professional

Number of Pages Required

4 page

Font styles to use
Sans Serif

Requirements
Must have
• Professional look and design like the examples i quoted above and a nice color theme. I do not have preferences but i like the fastroe.com and lumbek.com

```html
<!DOCTYPE html>
<html lang="en">
<head>
<meta charset="utf-8">
<title>Qarnelo — Online SEO Project Management</title>
<link rel="stylesheet" href="https://fonts.googleapis.com/css2?family=Raleway:wght@500;600;700&family=Lato:wght@400;700&display=swap">
<style>
  :root {
    --orange: #f7931e;
    --blue: #29a9e1;
    --blue-deep: #1e8fd0;
    --ink: #14181d;
    --panel: #1d2228;
    --white: #ffffff;
    --muted: #d7dde3;
  }
  * { box-sizing: border-box; margin: 0; padding: 0; }
  html, body { width: 742px; height: 1200px; overflow: hidden; background: var(--ink); }
  body { position: relative; font-family: 'Lato', sans-serif; color: var(--white); }
  .abs { position: absolute; }

  /* Hero */
  .hero {
    left: 0; top: 0; width: 742px; height: 589px;
    background:
      radial-gradient(ellipse 220px 170px at 370px 170px, rgba(196,128,60,.45), transparent 70%),
      radial-gradient(ellipse 300px 200px at 360px 420px, rgba(60,70,80,.6), transparent 75%),
      linear-gradient(180deg, #2a3340 0%, #232a33 45%, #1a1d22 80%, #111315 100%);
  }
  .header-rule { left: 0; top: 51px; width: 742px; height: 1px; background: rgba(255,255,255,.25); }
  .logo {
    left: 34px; top: 5px; width: 130px; height: 58px; background: var(--white);
    transform: rotate(-4deg); display: flex; align-items: center; justify-content: center; gap: 6px;
  }
  .logo-dot { width: 16px; height: 16px; border-radius: 50%; background: var(--orange); }
  .logo-name { font-family: 'Raleway', sans-serif; font-weight: 700; font-size: 19px; color: #3a3f45; }
  .nav { left: 284px; top: 0; height: 51px; display: flex; }
  .nav a {
    color: var(--white); text-decoration: none; font-size: 7px; letter-spacing: .2px;
    display: flex; align-items: center; padding: 0 13px; height: 51px;
  }
  .nav a.active { background: var(--blue); padding: 0 14px; }
  .login {
    left: 648px; top: 16px; width: 54px; height: 23px; background: var(--orange);
    font-size: 8px; display: flex; align-items: center; justify-content: center;
  }
  .hero-title {
    left: 0; top: 212px; width: 742px; text-align: center;
    font-family: 'Raleway', sans-serif; font-weight: 700; font-size: 24px;
  }
  .hero-text { left: 166px; top: 246px; width: 410px; text-align: center; font-size: 9px; line-height: 15.5px; }
  .cta {
    left: 313px; top: 307px; width: 117px; height: 28px; background: var(--orange);
    font-size: 8.5px; display: flex; align-items: center; justify-content: center;
  }
  .slider-arrow { top: 240px; }
  .dots { left: 355px; top: 429px; display: flex; gap: 8px; }
  .dots span { width: 7px; height: 7px; border-radius: 50%; background: var(--white); }
  .dots span.on { background: var(--orange); }
  .feature-rule { left: 0; top: 492px; width: 742px; height: 1px; background: rgba(255,255,255,.85); }
  .feature {
    width: 76px; height: 76px; border-radius: 50%; border: 2px solid var(--white);
    background: var(--blue); display: flex; align-items: center; justify-content: center; top: 454px;
  }
  .feature.orange { background: var(--orange); }
  .feature-label { top: 544px; width: 140px; text-align: center; font-family: 'Raleway', sans-serif; font-weight: 700; font-size: 10.5px; color: var(--blue); }
  .feature-label.orange { color: var(--orange); }

  /* Video band */
  .video-band {
    left: 0; top: 589px; width: 742px; height: 179px;
    background: linear-gradient(100deg, #2fa4dd 0%, #3aaee3 55%, #2c9fd9 100%);
  }
  .video-art { left: 330px; top: 589px; width: 380px; height: 179px;
    background: linear-gradient(160deg, rgba(255,255,255,.12), rgba(20,90,150,.15)); }
  .video-title { left: 83px; top: 620px; font-family: 'Raleway', sans-serif; font-weight: 600; font-size: 18px; }
  .video-text { left: 85px; top: 652px; width: 360px; font-size: 7.5px; line-height: 14px; }
  .view-all {
    left: 81px; top: 725px; width: 94px; height: 24px; background: var(--orange);
    font-size: 9px; font-weight: 700; display: flex; align-items: center; justify-content: center;
  }

  /* Services */
  .services { left: 0; top: 768px; width: 742px; height: 380px; background: linear-gradient(180deg, #1a1e23, #202429); }
  .services-title { left: 0; top: 792px; width: 742px; text-align: center; font-family: 'Raleway', sans-serif; font-weight: 600; font-size: 21px; }
  .services-title em { font-style: normal; color: var(--orange); }
  .services-text { left: 66px; top: 833px; width: 612px; text-align: center; font-size: 7.2px; line-height: 13px; }
  .card-media { top: 881px; width: 212px; height: 121px; }
  .card-title { top: 1017px; width: 212px; font-size: 10.5px; line-height: 14px; color: var(--blue); }
  .card-title.orange { color: var(--orange); }
  .card-text { top: 1047px; width: 212px; font-size: 7px; line-height: 10.5px; }
  .read-more {
    top: 1089px; width: 60px; height: 20px; border: 1px solid var(--white);
    font-size: 7px; display: flex; align-items: center; justify-content: center;
  }
  .read-more.orange { background: var(--orange); }
  .read-more.blue { background: var(--blue); }

  /* Footer */
  .footer { left: 0; top: 1148px; width: 742px; height: 52px; background: var(--orange); }
  .copyright { left: 30px; top: 1170px; font-size: 7.5px; }
  .social { left: 601px; top: 1170px; display: flex; gap: 16px; }
  .social span { width: 8px; height: 8px; border-radius: 50%; background: rgba(255,255,255,.8); }
</style>
</head>
<body>

<section class="abs hero" role="img" aria-label="Business team in a meeting room with a world map backdrop"></section>
<div class="abs header-rule"></div>

<div class="abs logo"><span class="logo-dot"></span><span class="logo-name">qarnelo</span></div>

<nav class="abs nav">
  <a class="active" href="#">HOME</a>
  <a href="#">FEATURES</a>
  <a href="#">PRICING</a>
  <a href="#">ABOUT US</a>
  <a href="#">CONTACT US</a>
</nav>
<div class="abs login">LOGIN</div>

<h1 class="abs hero-title">ONLINE SEO PROJECT MANAGEMENT</h1>
<p class="abs hero-text">Lorem ipsum dolor sit amet, consectetur adipiscing elit, sed do eiusmod tempor incididunt ut labore et dolore magna aliqua. Ut enim ad minim veniam, quis nostrud exercitation ullamco laboris nisi ut aliquip ex ea commodo consequat.</p>
<div class="abs cta">GET STARTING NOW</div>

<svg class="abs slider-arrow" style="left:25px" width="16" height="58" viewBox="0 0 16 58"><polyline points="14,1 2,29 14,57" fill="none" stroke="#fff" stroke-width="1.3"/></svg>
<svg class="abs slider-arrow" style="left:700px" width="16" height="58" viewBox="0 0 16 58"><polyline points="2,1 14,29 2,57" fill="none" stroke="#fff" stroke-width="1.3"/></svg>

<div class="abs dots"><span></span><span class="on"></span><span></span></div>

<div class="abs feature-rule"></div>

<div class="abs feature orange" style="left:68px">
  <svg width="34" height="34" viewBox="0 0 34 34" fill="none" stroke="#fff" stroke-width="4" stroke-linecap="round">
    <path d="M6 16a11 11 0 0 1 19-7"/><polyline points="26,3 26,10 19,10"/>
    <path d="M28 18a11 11 0 0 1-19 7"/><polyline points="8,31 8,24 15,24"/>
  </svg>
</div>
<div class="abs feature" style="left:243px">
  <svg width="30" height="30" viewBox="0 0 30 30"><rect x="5" y="5" width="20" height="20" rx="2" fill="#fff"/></svg>
</div>
<div class="abs feature" style="left:424px">
  <svg width="36" height="30" viewBox="0 0 36 30" fill="#fff"><rect x="10" y="2" width="14" height="11"/><rect x="2" y="15" width="14" height="12"/><rect x="19" y="15" width="14" height="12"/></svg>
</div>
<div class="abs feature" style="left:596px">
  <svg width="40" height="36" viewBox="0 0 40 36" fill="#fff"><rect x="13" y="2" width="14" height="33"/><rect x="3" y="14" width="9" height="21"/><rect x="28" y="18" width="10" height="17"/></svg>
</div>

<div class="abs feature-label orange" style="left:37px">INTEGRATED</div>
<div class="abs feature-label" style="left:212px">INTEGRATED</div>
<div class="abs feature-label" style="left:396px">COMING SOON</div>
<div class="abs feature-label" style="left:571px;top:541px">COMING SOON</div>

<section class="abs video-band"></section>
<div class="abs video-art" role="img" aria-label="Tablet showing a project dashboard"></div>
<h2 class="abs video-title">Video in Project Management</h2>
<p class="abs video-text">Lorem ipsum dolor sit amet, consectetur adipiscing elit, sed do eiusmod tempor incididunt ut labore et dolore magna aliqua. Ut enim ad minim veniam, quis nostrud exercitation ullamco laboris nisi ut aliquip ex ea commodo consequat. culpa qui officia deserunt</p>
<div class="abs view-all">VIEW ALL</div>
<svg class="abs" style="left:551px;top:648px" width="52" height="52" viewBox="0 0 52 52">
  <circle cx="26" cy="26" r="23.5" fill="none" stroke="#e6e6e6" stroke-width="4"/>
  <polygon points="20,14 37,26 20,38" fill="#e6e6e6"/>
</svg>

<section class="abs services"></section>
<h2 class="abs services-title">Our <em>Service</em></h2>
<p class="abs services-text">Lorem ipsum dolor sit amet, consectetur adipiscing elit, sed do eiusmod tempor incididunt ut labore et dolore magna aliqua. Ut enim ad minim veniam, quis nostrud exercitation ullam-co laboris. Duis aute irure dolor in reprehenderit in voluptate velit esse cillum dolore eu fugiat nulla pariatur.</p>

<div class="abs card-media" style="left:30px;background:linear-gradient(135deg,#e9eef2,#6f7e8c)" role="img" aria-label="Colleagues reviewing documents together"></div>
<div class="abs card-media" style="left:266px;background:linear-gradient(135deg,#5d6a74,#c9a987)" role="img" aria-label="Hand holding a phone showing the product"></div>
<div class="abs card-media" style="left:503px;background:linear-gradient(135deg,#6b4a33,#c9c2b8)" role="img" aria-label="Laptop and tablet on a wooden desk showing the product"></div>

<h3 class="abs card-title orange" style="left:30px;top:1019px">Organize, Collaborate and Deliver</h3>
<h3 class="abs card-title" style="left:266px;top:1016px">Best Project Management Tool for Digital Agencies</h3>
<h3 class="abs card-title" style="left:503px;top:1019px">Stress! Take it out of your projects</h3>

<p class="abs card-text" style="left:30px">Lorem ipsum dolor sit amet, consectetur adipiscing elit, sed do eiusmod tempor incididunt ut labore et dolore magna aliqua. Ut enim ad minim veniam, quis nostrud exercitation</p>
<p class="abs card-text" style="left:266px">Lorem ipsum dolor sit amet, consectetur adipiscing elit, sed do eiusmod tempor incididunt ut labore et dolore magna aliqua. Ut enim ad minim veniam, quis nostrud exercitation</p>
<p class="abs card-text" style="left:503px">Lorem ipsum dolor sit amet, consectetur adipiscing elit, sed do eiusmod tempor incididunt ut labore et dolore magna aliqua. Ut enim ad minim veniam, quis nostrud exercitation</p>

<div class="abs read-more orange" style="left:30px;top:1090px">READ MORE</div>
<div class="abs read-more blue" style="left:267px;top:1088px">READ MORE</div>
<div class="abs read-more blue" style="left:504px">READ MORE</div>

<footer class="abs footer"></footer>
<p class="abs copyright">All Rights Reserved. Copyrights @Company Name .2016</p>
<div class="abs social"><span></span><span></span><span></span><span></span><span></span></div>

</body>
</html>
```